San Francisco Pet Care Non Profit

Business Card Design for non profit organization.
We are a mobile pet care team who supports and attends to pets whose owners are homeless. Thanks for your help and creativity.

Industry/Entity Type

Non Profit

Contact Information for Business Card

Miriam Loxley
President
2817 Harrow Street, #516
San Francisco, CA 94187
phone: 415-782-3946
fax: 415-718-4053
miriam@warmpawvan.org
website: warmpawvan.org
facebook: facebook.com/WarmPawVan

Font styles to use
Serif
Sans Serif

Colors

Designer to choose colors to be used in the design.

Requirements
Must have
• above details and attached logo

```html
<!DOCTYPE html>
<html lang="en">
<head>
<meta charset="utf-8">
<title>WarmPawVan Business Card</title>
<link rel="stylesheet" href="https://fonts.googleapis.com/css2?family=Open+Sans:wght@400;600;700;800&display=swap">
<style>
  :root {
    --blue: #00a6e8;
    --black: #1b1b1b;
    --fold: #000000;
    --white: #ffffff;
    --grey: #5a5a5a;
    --faint: #d7effa;
    --backdrop: #e9e6e2;
  }
  * { box-sizing: border-box; margin: 0; padding: 0; }
  html, body { width: 1200px; height: 871px; overflow: hidden; }
  body {
    background: var(--backdrop);
    font-family: "Open Sans", Arial, sans-serif;
    position: relative;
  }
  .card {
    position: absolute;
    top: 276px;
    width: 540px;
    height: 320px;
    background: var(--white);
    box-shadow: 0 6px 18px rgba(0,0,0,.18);
    overflow: hidden;
  }
  .card--front { left: 40px; }
  .card--back { left: 620px; }

  /* Front */
  .front-mark {
    position: absolute;
    left: 150px; top: 40px;
    width: 150px; height: 150px;
    border-radius: 50%;
    background: var(--faint);
  }
  .front-brand {
    position: absolute;
    left: 0; right: 0; top: 118px;
    text-align: center;
    color: var(--blue);
    font-weight: 800;
    font-size: 58px;
    letter-spacing: -1px;
    line-height: 1;
  }
  .front-tagline {
    position: absolute;
    left: 0; right: 0; top: 186px;
    text-align: center;
    color: var(--black);
    font-weight: 800;
    font-size: 22px;
  }
  .front-web {
    position: absolute;
    left: 0; right: 0; top: 232px;
    text-align: center;
    color: var(--grey);
    font-size: 13px;
    letter-spacing: 4px;
  }

  /* Back */
  .back-shapes { position: absolute; inset: 0; }
  .back-logo {
    position: absolute;
    left: 26px; top: 150px;
    display: flex; align-items: center; gap: 10px;
  }
  .back-logo__dot {
    width: 36px; height: 36px;
    border-radius: 50%;
    border: 3px solid var(--blue);
  }
  .back-logo__name {
    color: var(--blue);
    font-weight: 700;
    font-size: 27px;
    line-height: 1;
    letter-spacing: -.5px;
  }
  .back-logo__tagline {
    color: var(--black);
    font-weight: 700;
    font-size: 11.5px;
    margin-top: 2px;
    padding-left: 30px;
  }
  .identity {
    position: absolute;
    right: 20px; top: 43px;
    text-align: right;
    color: var(--white);
    font-weight: 700;
    line-height: 1.15;
  }
  .identity__name { font-size: 17px; }
  .identity__role { font-size: 14px; }
  .contacts {
    position: absolute;
    right: 20px; top: 100px;
    list-style: none;
    text-align: right;
    color: var(--white);
    font-size: 13px;
    line-height: 23px;
  }
  .contacts li { display: flex; justify-content: flex-end; align-items: center; gap: 6px; }
  .contacts svg { width: 11px; height: 11px; fill: none; stroke: var(--white); stroke-width: 1.6; }
  .address {
    position: absolute;
    right: 20px; top: 236px;
    text-align: right;
    color: var(--white);
    font-size: 13px;
    line-height: 20px;
    font-style: normal;
  }
</style>
</head>
<body>

<section class="card card--front">
  <div class="front-mark"></div>
  <div class="front-brand">WarmPawVan</div>
  <div class="front-tagline">Mobile Pet Care Team</div>
  <div class="front-web">www.warmpawvan.org</div>
</section>

<section class="card card--back">
  <svg class="back-shapes" viewBox="0 0 540 320" width="540" height="320" aria-hidden="true">
    <polygon points="312,0 540,0 540,320 282,320" fill="var(--blue)"/>
    <polygon points="232,82 312,82 304,118" fill="var(--fold)"/>
    <rect x="232" y="40" width="308" height="42" fill="var(--black)"/>
  </svg>

  <div class="back-logo">
    <div class="back-logo__dot"></div>
    <div>
      <div class="back-logo__name">WarmPawVan</div>
      <div class="back-logo__tagline">Mobile Pet Care Team</div>
    </div>
  </div>

  <div class="identity">
    <div class="identity__name">Miriam Loxley</div>
    <div class="identity__role">President</div>
  </div>

  <ul class="contacts">
    <li><svg viewBox="0 0 12 12"><path d="M3 1l2 2.5-1.2 1.3a6 6 0 0 0 3.4 3.4L8.5 7 11 9l-1.2 2A9 9 0 0 1 1 2.2z"/></svg>415-782-3946</li>
    <li><svg viewBox="0 0 12 12"><rect x="3" y="1" width="6" height="3"/><rect x="1" y="4" width="10" height="5"/><rect x="3" y="7" width="6" height="4"/></svg>415-718-4053</li>
    <li><svg viewBox="0 0 12 12"><circle cx="6" cy="6" r="4.8"/></svg>/WarmPawVan</li>
    <li><svg viewBox="0 0 12 12"><rect x="1" y="2.5" width="10" height="7"/><path d="M1 2.5l5 4 5-4"/></svg>miriam@warmpawvan.org</li>
    <li><svg viewBox="0 0 12 12"><circle cx="6" cy="6" r="4.8"/><path d="M1.2 6h9.6M6 1.2c-2.5 3-2.5 6.6 0 9.6M6 1.2c2.5 3 2.5 6.6 0 9.6"/></svg>www.warmpawvan.org</li>
  </ul>

  <address class="address">
    2817 Harrow Street, #516<br>
    San Francisco, CA 94187
  </address>
</section>

</body>
</html>
```